Historic Church website

We want our church website to feel warm, historic, and clean, modern, and easy to navigate. Dont use the anchor

Current website: https://www.meadowlarkchapelhall.com/

Requirements
Should not have
• I would like to use the logo without the anchor

```html
<!DOCTYPE html>
<html lang="en">
<head>
<meta charset="utf-8">
<title>Meadowlark Chapel Hall</title>
<link href="https://fonts.googleapis.com/css2?family=Cormorant+Garamond:wght@400;500;600&family=EB+Garamond:wght@400;500&display=swap" rel="stylesheet">
<style>
:root{
  --tan:#d6a878;
  --tan-light:#e2bb8e;
  --tan-deep:#b98a5e;
  --brown:#8a5e3b;
  --olive:#6c6a62;
  --charcoal:#33322f;
  --ink:#1b1b1a;
  --card:#2a2a29;
  --cream:#f1e6d6;
  --muted:#b9b3a8;
}
*{margin:0;padding:0;box-sizing:border-box}
html,body{width:1200px;height:4288px;overflow:hidden}
body{background:var(--ink);color:var(--cream);font-family:"EB Garamond",Georgia,serif;position:relative}
section,header,footer{position:absolute;left:0;width:1200px;overflow:hidden}
.display{font-family:"Cormorant Garamond",Georgia,serif}
.photo{position:absolute;inset:0}
.ghost-word{position:absolute;font-family:"Cormorant Garamond",Georgia,serif;font-size:58px;letter-spacing:2px;color:rgba(255,255,255,.16);text-transform:uppercase;line-height:1}

/* hero */
.hero{top:0;height:660px}
.hero .photo{background:radial-gradient(ellipse at 50% 55%,#6a5544 0%,#45362b 45%,#231b16 100%)}
.hero .shade{position:absolute;inset:0;background:linear-gradient(180deg,rgba(0,0,0,.35),rgba(0,0,0,.15) 40%,rgba(0,0,0,.45))}
.nav{position:absolute;top:38px;left:0;width:1200px;display:flex;justify-content:center;align-items:center;gap:34px;font-size:13px;letter-spacing:1.5px;text-transform:uppercase}
.nav a{color:var(--cream);text-decoration:none}
.brand{display:flex;align-items:center;gap:10px;margin:0 22px;font-family:"Cormorant Garamond",Georgia,serif;font-size:24px;letter-spacing:1px;text-transform:none;color:var(--cream)}
.brand .dot{width:10px;height:10px;border-radius:50%;background:var(--cream)}
.hero-title{position:absolute;top:210px;width:1200px;text-align:center;font-family:"Cormorant Garamond",Georgia,serif;font-weight:500;font-size:66px;line-height:1.1;letter-spacing:2px;text-transform:uppercase}
.hero-title .accent{color:var(--tan);display:block}
.watch{position:absolute;top:382px;left:0;width:1200px;display:flex;justify-content:center;align-items:center;gap:12px;font-size:13px;letter-spacing:1.5px}
.watch span.ring{width:38px;height:38px;border:1.5px solid var(--cream);border-radius:50%;display:flex;align-items:center;justify-content:center}
.side-icon{position:absolute;left:14px;width:30px;height:30px;border:1.5px solid rgba(255,255,255,.6);border-radius:50%}

/* about */
.about{top:660px;height:700px;background:var(--olive)}
.about .ghost-word{left:-40px;top:420px;transform:rotate(-90deg);transform-origin:left top;top:600px;left:150px}
.about-photo{position:absolute;left:240px;top:88px;width:360px;height:480px;background:linear-gradient(160deg,#a9c2d6 0%,#e8e4da 45%,#8f7c62 100%)}
.about-copy{position:absolute;left:624px;top:96px;width:440px}
.about-copy h2{font-family:"Cormorant Garamond",Georgia,serif;font-weight:600;font-size:28px;line-height:1.2;color:#fff}
.about-copy h2 em{font-style:normal;color:var(--tan-light)}
.about-copy p{margin-top:30px;font-size:13.5px;line-height:1.65;color:#e9e3d8}
.btn-outline{display:inline-block;margin-top:34px;padding:10px 22px;border:1px solid var(--cream);font-size:11px;letter-spacing:1.5px;color:var(--cream)}

/* mission */
.mission{top:1360px;height:220px;background:var(--charcoal)}
.mission .col{position:absolute;top:74px;width:360px;display:flex;gap:16px}
.mission h3{font-size:15px;color:var(--tan);font-weight:500}
.mission p{margin-top:8px;font-size:13px;line-height:1.55;color:var(--muted)}

/* ministries */
.ministries{top:1580px;height:540px}
.ministries .photo{background:linear-gradient(100deg,#2d211a 0%,#5a4132 40%,#6f5646 70%,#3a2d25 100%)}
.ministries .ghost-word{right:60px;top:430px;text-align:right}
.ministry-card{position:absolute;left:96px;top:52px;width:504px;height:448px;background:var(--tan);padding:44px 40px;color:var(--ink)}
.ministry-card h2{font-family:"Cormorant Garamond",Georgia,serif;font-weight:600;font-size:28px;line-height:1.2}
.ministry-list{margin-top:34px;list-style:none}
.ministry-list li{display:flex;justify-content:space-between;align-items:center;padding:18px 0;border-bottom:1px solid rgba(27,27,26,.25);font-size:14px}

/* visit */
.visit{top:2120px;height:500px;background:var(--olive)}
.visit h2{position:absolute;top:40px;width:1200px;text-align:center;font-family:"Cormorant Garamond",Georgia,serif;font-weight:600;font-size:28px;color:#fff}
.visit h2 em{font-style:normal;color:var(--tan-light)}
.visit-main{position:absolute;left:260px;top:122px;width:300px;text-align:center}
.visit-main h3{margin-top:20px;font-family:"Cormorant Garamond",Georgia,serif;font-weight:600;font-size:26px;color:#fff}
.visit-main .time,.visit-item .time{font-size:13px;color:var(--cream);margin-top:8px}
.visit-main p{margin-top:10px;font-size:12.5px;line-height:1.5;color:#e2dccf}
.visit-divider{position:absolute;left:600px;top:120px;width:1px;height:310px;background:rgba(255,255,255,.3)}
.visit-item{position:absolute;left:640px;width:360px;display:flex;gap:22px}
.visit-item .txt{text-align:center;flex:1}
.visit-item h3{font-family:"Cormorant Garamond",Georgia,serif;font-weight:600;font-size:24px;color:var(--tan-light)}
.visit-item p{font-size:12.5px;line-height:1.5;color:#e2dccf}

/* events */
.events{top:2620px;height:540px;background:var(--ink)}
.events h2{position:absolute;top:58px;width:1200px;text-align:center;font-family:"Cormorant Garamond",Georgia,serif;font-weight:600;font-size:28px;color:var(--tan)}
.event{position:absolute;top:140px;width:264px;height:320px;background:var(--card);text-align:center;padding-top:74px}
.event .day,.event .date{font-family:"Cormorant Garamond",Georgia,serif;font-size:30px;line-height:1.15;color:#f3ece1}
.event .time{margin-top:40px;font-size:13px;color:var(--muted)}
.event .name{margin-top:16px;font-size:13px;line-height:1.45;color:var(--muted)}
.arrow{position:absolute;top:282px;width:40px;height:40px;border-radius:50%;background:#0c0c0c;display:flex;align-items:center;justify-content:center}

/* newsletter */
.newsletter{top:3160px;height:480px}
.newsletter .photo{background:linear-gradient(120deg,#3b2a1d 0%,#7a5a3c 35%,#a57f55 60%,#4a3526 100%)}
.newsletter .ghost-word{left:140px;top:390px}
.news-card{position:absolute;left:580px;top:88px;width:560px;height:372px;background:var(--tan);padding:44px 44px;color:var(--ink)}
.news-card h2{font-family:"Cormorant Garamond",Georgia,serif;font-weight:600;font-size:26px}
.form-row{display:flex;gap:16px;margin-top:22px}
.field{flex:1}
.field label{display:block;font-size:11.5px;margin-bottom:6px}
.field .input{height:34px;background:var(--tan-deep);opacity:.8}
.btn-solid{display:inline-block;margin-top:24px;padding:10px 32px;background:var(--brown);color:var(--cream);font-size:11px;letter-spacing:1.5px}

/* footer */
.site-footer{top:3640px;height:648px;background:var(--ink)}
.footer-brand{position:absolute;top:44px;width:1200px;display:flex;justify-content:center;align-items:center;gap:10px;font-family:"Cormorant Garamond",Georgia,serif;font-size:30px;color:var(--cream)}
.footer-brand .dot{width:12px;height:12px;border-radius:50%;background:var(--cream)}
.footer-cats{position:absolute;left:210px;top:250px}
.footer-cats h4,.footer-connect h4{font-size:12px;color:var(--cream);font-weight:500}
.footer-cats ul{list-style:none;margin-top:12px}
.footer-cats li{font-size:11.5px;color:var(--muted);line-height:1.75}
.footer-contact{position:absolute;left:400px;top:240px;width:400px;text-align:center}
.contact-block{margin-bottom:26px}
.contact-block .ico{width:30px;height:30px;border:1px solid var(--tan);border-radius:50%;margin:0 auto 8px;display:flex;align-items:center;justify-content:center}
.contact-block .lbl{font-size:11px;letter-spacing:1.5px;color:var(--tan)}
.contact-block .val{font-size:12.5px;color:var(--cream);margin-top:4px;line-height:1.45}
.footer-line{position:absolute;left:599px;top:250px;width:1px;height:0}
.footer-connect{position:absolute;right:210px;top:250px;text-align:left}
.socials{display:flex;gap:10px;margin-top:12px}
.socials span{width:14px;height:14px;border-radius:50%;background:var(--muted)}
.copyright{position:absolute;bottom:40px;width:1200px;text-align:center;font-size:10.5px;letter-spacing:1.5px;color:#7c776f}
</style>
</head>
<body>

<header class="hero">
  <div class="photo" role="img" aria-label="Photograph of a historic church interior with wooden chairs, a table and framed pictures"></div>
  <div class="shade"></div>
  <nav class="nav">
    <a href="#">Home</a>
    <a href="#">About MCH</a>
    <a href="#">Ministries</a>
    <span class="brand"><span class="dot"></span>Meadowlark Chapel Hall</span>
    <a href="#">Bible Studies</a>
    <a href="#">Sermon Library</a>
    <a href="#">Donate</a>
  </nav>
  <span class="side-icon" style="top:210px"></span>
  <span class="side-icon" style="top:590px"></span>
  <h1 class="hero-title">Historic Church, Ancient Faith<span class="accent">Eternal Truth</span></h1>
  <div class="watch">
    <span class="ring"><svg width="12" height="14" viewBox="0 0 12 14"><path d="M1 1 L11 7 L1 13 Z" fill="#f1e6d6"/></svg></span>
    <span>WATCH VIDEO</span>
  </div>
</header>

<section class="about">
  <div class="ghost-word">About MCH</div>
  <div class="about-photo" role="img" aria-label="Photograph of the white chapel facade with an arched doorway beside a tall building"></div>
  <div class="about-copy">
    <h2>Meadowlark Chapel Hall is an <em>independent Christian church</em> in the Protestant tradition.</h2>
    <p>Our church was founded on the doctrine of Christ and has faithfully served this city for many generations. We hold to the authority of Scripture, the grace of God in the gospel, and the call to love one another well. Each week we gather to worship, to pray, and to learn from the Word together, and we welcome every neighbour who walks through our doors to find rest, hope and a family of faith.</p>
    <span class="btn-outline">LEARN MORE</span>
  </div>
</section>

<section class="mission">
  <div class="col" style="left:240px">
    <svg width="26" height="26" viewBox="0 0 26 26" fill="none" stroke="#d6a878" stroke-width="1.5"><path d="M13 2v22M6 9h14"/></svg>
    <div><h3>Our mission</h3><p>Our mission is to glorify the Triune God and make disciples of Jesus Christ.</p></div>
  </div>
  <div class="col" style="left:624px">
    <svg width="28" height="24" viewBox="0 0 28 24" fill="none" stroke="#d6a878" stroke-width="1.5"><path d="M14 5c-4-3-9-3-12-1v17c3-2 8-2 12 1c4-3 9-3 12-1V4c-3-2-8-2-12 1zM14 5v17"/></svg>
    <div><h3>Our purpose</h3><p>To share the good news of the gospel and teach the historic doctrines of the Christian faith, so that all may grow in grace.</p></div>
  </div>
</section>

<section class="ministries">
  <div class="photo" role="img" aria-label="Photograph of a warm church lounge with armchairs, shutters and bookshelves"></div>
  <div class="ghost-word">MCH<br>Ministries</div>
  <div class="ministry-card">
    <h2>God has blessed Meadowlark Chapel Hall with some very gifted people with hearts for service!</h2>
    <ul class="ministry-list">
      <li>Small Groups &amp; Bible Studies<svg width="8" height="12" viewBox="0 0 8 12"><path d="M1 1l5 5-5 5" stroke="#1b1b1a" stroke-width="1.5" fill="none"/></svg></li>
      <li>Men's Ministry<svg width="8" height="12" viewBox="0 0 8 12"><path d="M1 1l5 5-5 5" stroke="#1b1b1a" stroke-width="1.5" fill="none"/></svg></li>
      <li>Women's Ministry<svg width="8" height="12" viewBox="0 0 8 12"><path d="M1 1l5 5-5 5" stroke="#1b1b1a" stroke-width="1.5" fill="none"/></svg></li>
      <li>Kids Church<svg width="8" height="12" viewBox="0 0 8 12"><path d="M1 1l5 5-5 5" stroke="#1b1b1a" stroke-width="1.5" fill="none"/></svg></li>
    </ul>
  </div>
</section>

<section class="visit">
  <h2>Visit us <em>this sunday!</em></h2>
  <div class="visit-main">
    <svg width="110" height="100" viewBox="0 0 110 100" fill="none" stroke="#f1e6d6" stroke-width="2">
      <rect x="6" y="14" width="98" height="80" rx="6"/>
      <path d="M6 34h98M30 6v16M80 6v16"/>
      <path d="M55 44v40M44 56h22"/>
    </svg>
    <h3>Morning worship service</h3>
    <div class="time">10:00 AM</div>
    <p>Sunday morning worship and sermon.<br>Also join us for the main service.</p>
  </div>
  <div class="visit-divider"></div>
  <div class="visit-item" style="top:140px">
    <svg width="34" height="34" viewBox="0 0 34 34" fill="none" stroke="#f1e6d6" stroke-width="1.5"><path d="M6 30V12l11-8 11 8v18zM13 30v-9h8v9"/></svg>
    <div class="txt"><h3>All church lunch</h3><div class="time">12:15 PM</div><p>• Family Room •<br>Please join us for lunch after the service.<br>Everyone is welcome!</p></div>
  </div>
  <div class="visit-item" style="top:300px">
    <svg width="34" height="34" viewBox="0 0 34 34" fill="none" stroke="#f1e6d6" stroke-width="1.5"><path d="M17 8c-4-3-10-3-14-1v20c4-2 10-2 14 1c4-3 10-3 14-1V7c-4-2-10-2-14 1zM17 8v20"/></svg>
    <div class="txt"><h3>Afternoon adult bible study</h3><div class="time">1:15 PM</div><p>• Prayer Room •<br>TBA</p></div>
  </div>
</section>

<section class="events">
  <h2>Upcoming events</h2>
  <span class="arrow" style="left:28px"><svg width="10" height="14" viewBox="0 0 10 14"><path d="M8 1L2 7l6 6" stroke="#f1e6d6" stroke-width="1.8" fill="none"/></svg></span>
  <div class="event" style="left:180px"><div class="day">Wed</div><div class="date">Jan 10, 2026</div><div class="time">7:00 PM</div><div class="name">Wednesday night<br>bible study</div></div>
  <div class="event" style="left:468px"><div class="day">Sun</div><div class="date">Jan 17, 2026</div><div class="time">10:00 AM</div><div class="name">Sunday service</div></div>
  <div class="event" style="left:756px"><div class="day">Wed</div><div class="date">Jan 28, 2026</div><div class="time">7:00 PM</div><div class="name">Wednesday night<br>bible study</div></div>
  <span class="arrow" style="left:1132px"><svg width="10" height="14" viewBox="0 0 10 14"><path d="M2 1l6 6-6 6" stroke="#f1e6d6" stroke-width="1.8" fill="none"/></svg></span>
</section>

<section class="newsletter">
  <div class="photo" role="img" aria-label="Photograph of an antique map on a desk with a clock, compass and old books"></div>
  <div class="ghost-word">Newsletter</div>
  <div class="news-card">
    <h2>Sign up for our weekly newsletter</h2>
    <div class="form-row">
      <div class="field"><label>First Name</label><div class="input"></div></div>
      <div class="field"><label>Last Name</label><div class="input"></div></div>
    </div>
    <div class="form-row">
      <div class="field"><label>Email</label><div class="input"></div></div>
    </div>
    <span class="btn-solid">SUBSCRIBE</span>
  </div>
</section>

<footer class="site-footer">
  <div class="footer-brand"><span class="dot"></span>Meadowlark Chapel Hall</div>
  <div class="footer-cats">
    <h4>Categories</h4>
    <ul><li>Home</li><li>About MCH</li><li>Ministries</li><li>Bible Studies</li><li>Sermon Library</li><li>Donate</li></ul>
  </div>
  <div class="footer-contact">
    <div class="contact-block">
      <div class="ico"><svg width="14" height="14" viewBox="0 0 14 14"><path d="M3 1l2 3-1.5 1.5a8 8 0 0 0 5 5L10 9l3 2-1 2c-6 0-11-5-11-11z" fill="#d6a878"/></svg></div>
      <div class="lbl">CALL US</div><div class="val">(555) 014-2290</div>
    </div>
    <div class="contact-block">
      <div class="ico"><svg width="14" height="12" viewBox="0 0 14 12" fill="none" stroke="#d6a878" stroke-width="1.3"><rect x="1" y="1" width="12" height="10"/><path d="M1 1l6 5 6-5"/></svg></div>
      <div class="lbl">EMAIL US</div><div class="val">info@meadowlarkchapelhall.com</div>
    </div>
    <div class="contact-block">
      <div class="ico"><svg width="12" height="15" viewBox="0 0 12 15"><path d="M6 1a5 5 0 0 0-5 5c0 4 5 8 5 8s5-4 5-8a5 5 0 0 0-5-5zm0 7a2 2 0 1 1 0-4 2 2 0 0 1 0 4z" fill="#d6a878"/></svg></div>
      <div class="lbl">VISIT US</div><div class="val">2140 Larkspur Avenue<br>Fairhaven, California 90000</div>
    </div>
  </div>
  <div class="footer-connect">
    <h4>Connect with us</h4>
    <div class="socials"><span></span><span></span><span></span><span></span></div>
  </div>
  <div class="copyright">COPYRIGHT © 2026 MEADOWLARK CHAPEL HALL. ALL RIGHTS RESERVED.</div>
</footer>

</body>
</html>
```